Tour agency for FIT and groups need a business card design

We need a business card design for a tour agency company that is based in Perth called" BRISK NO", we aim to provide customise, unique and seamless travel arrangement for FIT and groups. We serve both high profile businessperson, government authorities, business partners, executives and investors. The name card should be more professional looking.
Updates

Project Deadline Extended Reason: Have some changes that needed to make, director will be back to office on Monday, sorry for the inconvenience cause. Added Saturday, May 6, 2017

Target Market(s)

High profile businessperson, government authorities, business partners, executives and investors.

Industry/Entity Type

Tourism

Contact Information for Business Card

Brisk NO
Level 1, 214 Marlowe Avenue, Dunreath NO, 6120
www.briskno.com.au

Font styles to use
Serif

Colors

Designer to choose colors to be used in the design.

Requirements
Must have
• My project must have a company logo
Nice to have
• a more professional and solid yet friendly name card design. We may want to include chinese name in the name card as well. Edge of the card can be filled with gold and we think that transparent name cards are interesting.

```html
<!DOCTYPE html>
<html lang="en">
<head>
<meta charset="utf-8">
<title>Brisk NO — Business Card</title>
<link rel="stylesheet" href="https://fonts.googleapis.com/css2?family=Open+Sans:wght@400&display=swap">
<style>
  :root {
    --stage-mid: #5c5857;
    --stage-light: #6e6968;
    --stage-dark: #2b2a2a;
    --stage-deep: #1f1f1f;
    --front-top: #2e2e2e;
    --front-mid: #4a4948;
    --front-bottom: #252525;
    --back-left-a: #1b1b1b;
    --back-left-b: #403e3d;
    --back-right-a: #474342;
    --back-right-b: #b8b4b3;
    --divider: #6a6564;
    --brand-blue: #2aa7df;
    --title-grey: #d3d8d8;
    --text-white: #ffffff;
    --text-soft: #e3e3e3;
  }
  html, body {
    margin: 0;
    padding: 0;
    overflow: hidden;
  }
  body {
    width: 1150px;
    height: 1200px;
    position: relative;
    background: var(--stage-mid);
    font-family: "Open Sans", sans-serif;
  }
  .stage-step {
    position: absolute;
  }
  .stage-step--upper-left { left: 0; top: 0; width: 300px; height: 205px; background: var(--stage-dark); }
  .stage-step--upper-right { left: 864px; top: 0; width: 286px; height: 193px; background: var(--stage-dark); }
  .stage-step--mid-left { left: 0; top: 205px; width: 90px; height: 193px; background: #4a4746; }
  .stage-step--mid-right { left: 1072px; top: 193px; width: 78px; height: 200px; background: #4a4746; }
  .stage-step--low-left { left: 0; top: 398px; width: 300px; height: 202px; background: var(--stage-light); }
  .stage-step--low-right { left: 864px; top: 393px; width: 286px; height: 207px; background: var(--stage-light); }
  .stage-step--column {
    left: 300px; top: 0; width: 564px; height: 600px;
    background: linear-gradient(180deg, var(--stage-deep) 0%, #333 55%, var(--stage-deep) 100%);
  }

  .card-front {
    position: absolute;
    left: 90px; top: 68px;
    width: 982px; height: 454px;
    background: linear-gradient(180deg, var(--front-top) 0%, var(--front-mid) 62%, var(--front-bottom) 100%);
  }
  .brand-name {
    position: absolute;
    margin: 0;
    color: var(--brand-blue);
    font-weight: 400;
    white-space: nowrap;
    line-height: 1;
  }
  .card-front .brand-name {
    left: 0; right: 0; top: 160px;
    text-align: center;
    font-size: 112px;
  }

  .card-back-left {
    position: absolute;
    left: 0; top: 600px;
    width: 514px; height: 600px;
    background: linear-gradient(90deg, var(--back-left-a) 0%, var(--back-left-b) 100%);
  }
  .card-back-left .brand-name {
    left: 40px; top: 270px;
    font-size: 54px;
  }
  .address {
    position: absolute;
    left: 0; width: 540px; top: 448px;
    margin: 0;
    text-align: center;
    color: var(--text-white);
    font-size: 34px;
    line-height: 48px;
  }

  .card-divider {
    position: absolute;
    left: 514px; top: 600px;
    width: 21px; height: 600px;
    background: linear-gradient(180deg, var(--divider) 0%, #3a3838 100%);
  }

  .card-back-right {
    position: absolute;
    left: 535px; top: 600px;
    width: 615px; height: 600px;
    background: linear-gradient(90deg, var(--back-right-a) 0%, #6a6564 55%, var(--back-right-b) 100%);
  }
  .company-title {
    position: absolute;
    left: 0; right: 0; top: 68px;
    margin: 0;
    text-align: center;
    color: var(--title-grey);
    font-weight: 400;
    font-size: 70px;
    line-height: 1;
  }
  .contact-list {
    position: absolute;
    left: 0; right: 0; top: 465px;
    margin: 0; padding: 0;
    list-style: none;
    text-align: center;
    color: var(--text-soft);
    font-size: 25px;
    line-height: 34px;
  }
</style>
</head>
<body>
  <div class="stage-step stage-step--upper-left"></div>
  <div class="stage-step stage-step--upper-right"></div>
  <div class="stage-step stage-step--mid-left"></div>
  <div class="stage-step stage-step--mid-right"></div>
  <div class="stage-step stage-step--low-left"></div>
  <div class="stage-step stage-step--low-right"></div>
  <div class="stage-step stage-step--column"></div>

  <section class="card-front" aria-label="Card front">
    <p class="brand-name">Brisk NO</p>
  </section>

  <section class="card-back-left" aria-label="Card back, brand side">
    <p class="brand-name">Brisk NO</p>
    <p class="address">Level 1, 214 Marlowe Avenue,</p>
  </section>

  <div class="card-divider"></div>

  <section class="card-back-right" aria-label="Card back, contact side">
    <h1 class="company-title">Brisk NO</h1>
    <ul class="contact-list">
      <li>Email: someone@briskno.com.au</li>
      <li>Mobile: +1(555) 014-2273</li>
      <li>www.briskno.com.au</li>
    </ul>
  </section>
</body>
</html>
```